Real Estate Card Design

I need a new business card! Below you will find my headshot, the company logo and a copy of my previous business card.

The card must contain the following information:

Dana Welch
Sales Representative
FAIR HARBOUR HOMES REALTY INC BROKERGE
204-517 Maple Ave E, Oshawa ON L1G 4K7
Cell: 905-618-4037 Office:905-481-2696
www.danawelch.com dana@movewithwelch.ca

I would like the card to portray security and class all the while being fresh and contemporary. I hold the key....

```html
<!DOCTYPE html>
<html lang="en">
<head>
<meta charset="utf-8">
<title>Dana Welch – Business Card</title>
<link rel="stylesheet" href="https://fonts.googleapis.com/css2?family=Italianno&family=Roboto:wght@300;400;500&display=swap">
<style>
  :root{
    --backdrop:#f4b081;
    --ink-dark:#2b3230;
    --sky-blue:#29b4e4;
    --paper:#f7f7f5;
    --text-grey:#6a6a6a;
    --white:#ffffff;
  }
  *{box-sizing:border-box;margin:0;padding:0}
  html,body{width:1200px;height:1200px;overflow:hidden}
  body{background:var(--backdrop);font-family:"Roboto",sans-serif;position:relative}

  .card{position:absolute;top:250px;width:440px;height:700px;overflow:hidden;box-shadow:0 18px 40px rgba(0,0,0,.18)}
  .card--front{left:140px;background:var(--ink-dark)}
  .card--back{left:620px;background:var(--sky-blue)}

  .card__frame{position:absolute;inset:22px;border:2px solid var(--white)}

  .headshot{position:absolute;left:24px;right:24px;top:24px;height:420px;
    background:radial-gradient(ellipse at 50% 40%,#4a4c48 0%,#2f3532 55%,#262b29 100%)}

  .city-band{position:absolute;left:0;right:0;bottom:0}
  .card--front .city-band{height:240px;background:var(--paper)}
  .card--back .city-band{height:170px;background:var(--white)}

  .front__text{position:absolute;left:0;right:0;bottom:44px;text-align:center}
  .agent-name{font-family:"Italianno",cursive;color:var(--sky-blue);font-size:84px;line-height:1;letter-spacing:1px}
  .agent-title{color:var(--text-grey);font-weight:300;font-size:23px;margin-top:8px}
  .agent-cell{color:var(--text-grey);font-weight:300;font-size:23px;margin-top:6px;display:flex;justify-content:center;align-items:center;gap:6px}
  .agent-cell svg{width:14px;height:22px}

  .contact{position:absolute;left:0;right:0;top:92px;text-align:center;color:var(--white);font-weight:500;font-size:21px;line-height:1.25}
  .contact__item{margin-bottom:22px}
  .contact__icon{display:block;margin:0 auto 6px;width:22px;height:22px}

  .brand{position:absolute;left:0;right:0;bottom:62px;display:flex;justify-content:center;align-items:center;gap:10px}
  .brand__mark{width:26px;height:26px;background:var(--sky-blue)}
  .brand__name{font-family:"Roboto",sans-serif;font-weight:500;font-size:15px;color:var(--ink-dark);letter-spacing:1px;line-height:1.2;text-align:left}
</style>
</head>
<body>

<section class="card card--front">
  <div class="headshot" role="img" aria-label="Portrait of agent holding a house key"></div>
  <div class="card__frame"></div>
  <div class="city-band" role="img" aria-label="City skyline silhouette"></div>
  <div class="front__text">
    <div class="agent-name">Dana Welch</div>
    <div class="agent-title">Sales Representative</div>
    <div class="agent-cell">
      <svg viewBox="0 0 14 22" aria-hidden="true"><rect x="1.5" y="1.5" width="11" height="19" rx="2" fill="none" stroke="#29b4e4" stroke-width="2"/><rect x="5" y="17" width="4" height="1.6" fill="#29b4e4"/></svg>
      905-618-4037
    </div>
  </div>
</section>

<section class="card card--back">
  <div class="card__frame"></div>
  <div class="contact">
    <div class="contact__item">
      <svg class="contact__icon" viewBox="0 0 24 24" aria-hidden="true"><path d="M12 2a7 7 0 0 0-7 7c0 5 7 13 7 13s7-8 7-13a7 7 0 0 0-7-7zm0 9.5A2.5 2.5 0 1 1 12 6.5a2.5 2.5 0 0 1 0 5z" fill="#fff"/></svg>
      204-517 Maple Ave E,<br>Oshawa ON L1G 4K7
    </div>
    <div class="contact__item">
      <svg class="contact__icon" viewBox="0 0 24 24" aria-hidden="true"><path d="M3 9c0-3 4-5 9-5s9 2 9 5v2h-5V9H8v2H3zM6 12h12l2 8H4z" fill="#fff"/></svg>
      905-481-2696
    </div>
    <div class="contact__item">
      <svg class="contact__icon" viewBox="0 0 24 24" aria-hidden="true"><circle cx="12" cy="12" r="9" fill="none" stroke="#fff" stroke-width="2"/><ellipse cx="12" cy="12" rx="4" ry="9" fill="none" stroke="#fff" stroke-width="1.6"/><line x1="3" y1="12" x2="21" y2="12" stroke="#fff" stroke-width="1.6"/></svg>
      www.danawelch.com
    </div>
    <div class="contact__item">
      <svg class="contact__icon" viewBox="0 0 24 24" aria-hidden="true"><rect x="2" y="5" width="20" height="14" fill="#fff"/><polyline points="2,5 12,13 22,5" fill="none" stroke="#29b4e4" stroke-width="1.6"/></svg>
      dana@movewithwelch.ca
    </div>
  </div>
  <div class="city-band" role="img" aria-label="City skyline silhouette"></div>
  <div class="brand">
    <span class="brand__mark" aria-hidden="true"></span>
    <span class="brand__name">FAIR HARBOUR HOMES<br>REALTY INC BROKERGE</span>
  </div>
</section>

</body>
</html>
```